Invite to The Halvorsen Project

You’re Cordially Invited
To a Sunset Celebration Honoring the Launch of The Halvorsen

Date: Thursday, May 15
Time: 5:30 PM – 7:30 PM
Location: The Halvorsen, 214 Quillfield Street, East Boston

Please join us for an elegant evening of connection and celebration as we unveil The Halvorsen Project.
Enjoy private tours of Units 3 and 4, along with our breathtaking roof deck offering sweeping views of East Boston at sunset.

Sip curated selections of beer and wine and savor light seasonal bites as you mingle with colleagues and guests.

Feel free to bring clients, friends, or family — all are welcome!

Kindly RSVP to:
Marisol Penwarden, Larchmont Realty
📧 Marisol@larchmontexample.com

Please include logo, classic design, and attachments. Colors navy, gold, white

```html
<!DOCTYPE html>
<html lang="en">
<head>
<meta charset="utf-8">
<title>Sunset Celebration – The Halvorsen Project</title>
<link rel="stylesheet" href="https://fonts.googleapis.com/css2?family=Cinzel:wght@400;700;900&family=Lato:wght@400;700&family=Libre+Baskerville:ital,wght@1,700&display=swap">
<style>
  :root {
    --navy: #1f2a4f;
    --navy-deep: #17203f;
    --blue: #3a5bb3;
    --gold: #e5b85a;
    --gold-light: #f6dea0;
    --gold-pale: #fbf0cf;
    --white: #ffffff;
    --stage: #d9d9d9;
  }
  * { margin: 0; padding: 0; box-sizing: border-box; }
  html, body { width: 1200px; height: 751px; overflow: hidden; }
  body { background: var(--stage); position: relative; font-family: "Lato", sans-serif; }

  .invite {
    position: absolute; left: 310px; top: 0; width: 580px; height: 751px;
    overflow: hidden; background: var(--navy); color: var(--white);
  }
  .invite__backdrop { position: absolute; inset: 0; }
  .invite__photo {
    position: absolute; left: 150px; top: 60px; width: 430px; height: 520px;
    background: radial-gradient(ellipse at 60% 40%, rgba(240,200,130,.45), rgba(90,90,110,.15) 55%, transparent 75%);
  }
  .invite__glasses {
    position: absolute; left: 10px; top: 560px; width: 220px; height: 180px;
    background: radial-gradient(ellipse at 45% 55%, rgba(229,184,90,.55), rgba(229,184,90,.12) 55%, transparent 75%);
  }

  .brand { position: absolute; left: 0; width: 580px; top: 28px; text-align: center; }
  .brand__mark {
    width: 64px; height: 64px; border: 3px solid var(--gold); border-radius: 50%;
    margin: 0 auto 12px;
  }
  .brand__name {
    font-family: "Cinzel", serif; font-weight: 400; color: var(--gold);
    font-size: 28px; line-height: 1.1; letter-spacing: 1px;
  }

  .headline { position: absolute; left: 26px; top: 190px; font-family: "Cinzel", serif; line-height: 1; }
  .headline__intro { font-size: 17px; font-weight: 400; }
  .headline__sunset { font-size: 60px; font-weight: 900; color: var(--gold); margin-top: 2px; }
  .headline__celebration { font-size: 37px; font-weight: 900; margin-top: -2px; }
  .headline__honoring { font-size: 18.5px; font-weight: 400; margin-top: 2px; }
  .headline__name { font-size: 31px; font-weight: 700; color: var(--gold); margin-top: 1px; }

  .details { position: absolute; left: 26px; top: 398px; width: 300px; font-size: 12.5px; line-height: 1.15; letter-spacing: .4px; }
  .details p + p { margin-top: 10px; }

  .welcome-band {
    position: absolute; left: 0; top: 510px; width: 250px; height: 52px;
    background: linear-gradient(90deg, var(--blue), rgba(58,91,179,.85) 60%, rgba(58,91,179,0));
    padding: 10px 0 0 26px;
    font-family: "Libre Baskerville", serif; font-style: italic; font-weight: 700;
    font-size: 12px; line-height: 1.35;
  }

  .perks {
    position: absolute; left: 378px; top: 256px; width: 176px; height: 176px; border-radius: 50%;
    background: radial-gradient(circle at 45% 40%, #2e3b66, var(--navy-deep));
    border: 5px solid var(--gold);
    box-shadow: 0 0 0 2px #8a6a24, 0 6px 14px rgba(0,0,0,.35);
    display: flex; align-items: center; justify-content: center; text-align: center;
    padding: 20px; font-size: 13px; line-height: 1.12; letter-spacing: .3px;
  }

  .when { position: absolute; right: 24px; top: 454px; text-align: right; font-family: "Cinzel", serif; color: var(--navy); line-height: 1; }
  .when__day { font-size: 29px; font-weight: 400; }
  .when__date { font-size: 30px; font-weight: 900; }
  .when__rule { height: 2px; width: 180px; margin: 6px 0 6px auto; background: linear-gradient(90deg, transparent, var(--gold-pale)); }
  .when__time { font-size: 30px; font-weight: 900; color: var(--white); line-height: .95; }
  .when__place { font-size: 17px; font-weight: 700; margin-top: 12px; line-height: 1; }

  .rsvp {
    position: absolute; right: 0; top: 664px; width: 390px; height: 87px;
    background: linear-gradient(90deg, rgba(246,222,160,0), var(--gold-light) 35%, var(--gold-pale));
    padding: 6px 24px 0 0; text-align: right; color: var(--navy);
  }
  .rsvp__label { font-family: "Cinzel", serif; font-size: 12px; }
  .rsvp__name { font-family: "Cinzel", serif; font-weight: 900; font-size: 19px; line-height: 1.05; margin-top: 4px; }
  .rsvp__company { font-family: "Cinzel", serif; font-weight: 400; font-size: 17px; line-height: 1; }
  .rsvp__email { font-size: 9.5px; margin-top: 4px; }
</style>
</head>
<body>
<main class="invite">
  <svg class="invite__backdrop" width="580" height="751" viewBox="0 0 580 751" aria-hidden="true">
    <defs>
      <linearGradient id="goldField" x1="0" y1="0" x2="1" y2="1">
        <stop offset="0" stop-color="#f7e2a8"/>
        <stop offset=".5" stop-color="#e9c06a"/>
        <stop offset="1" stop-color="#d9a94e"/>
      </linearGradient>
      <linearGradient id="navyField" x1="0" y1="0" x2="0" y2="1">
        <stop offset="0" stop-color="#25305a"/>
        <stop offset="1" stop-color="#1a2345"/>
      </linearGradient>
    </defs>
    <rect width="580" height="751" fill="url(#navyField)"/>
    <polygon points="0,0 150,0 0,260" fill="#3a5bb3"/>
    <polygon points="150,0 175,0 0,300 0,260" fill="#2d4590" opacity=".6"/>
    <polygon points="540,0 580,0 580,40 300,560" fill="#3a5bb3" opacity=".55"/>
    <polygon points="575,0 580,0 580,6 320,470" fill="#6d8be0" opacity=".7"/>
    <polygon points="580,60 580,751 110,751" fill="url(#goldField)"/>
  </svg>
  <div class="invite__photo" role="img" aria-label="Photograph of a tree silhouetted against an East Boston sunset"></div>
  <div class="invite__glasses" role="img" aria-label="Illustration of two sparkling gold champagne glasses toasting"></div>

  <header class="brand">
    <div class="brand__mark"></div>
    <p class="brand__name">Larchmont Realty</p>
  </header>

  <h1 class="headline">
    <span style="display:block" class="headline__intro">You’re Cordially Invited to a</span>
    <span style="display:block" class="headline__sunset">SUNSET</span>
    <span style="display:block" class="headline__celebration">CELEBRATION</span>
    <span style="display:block" class="headline__honoring">Honoring the Launch of</span>
    <span style="display:block" class="headline__name">THE HALVORSEN</span>
  </h1>

  <section class="details">
    <p>Please join us for an elegant evening of connection and celebration as we unveil The Halvorsen Project.</p>
    <p>Enjoy private tours of Units 3 and 4, along with our breathtaking roof deck offering sweeping views of East Boston at sunset.</p>
  </section>

  <p class="welcome-band">Feel free to bring clients, friends,<br>or family — all are welcome!</p>

  <p class="perks">Sip curated selections of beer and wine and savor light seasonal bites as you mingle with colleagues and guests.</p>

  <section class="when">
    <p class="when__day">THURSDAY</p>
    <p class="when__date">MAY 15TH</p>
    <div class="when__rule"></div>
    <p class="when__time">5:30 PM<br>7:30 PM</p>
    <p class="when__place">The Halvorsen,<br>214 Quillfield Street,<br>East Boston</p>
  </section>

  <footer class="rsvp">
    <p class="rsvp__label">Kindly RSVP to:</p>
    <p class="rsvp__name">MARISOL PENWARDEN</p>
    <p class="rsvp__company">LARCHMONT REALTY</p>
    <p class="rsvp__email">Marisol@larchmontexample.com</p>
  </footer>
</main>
</body>
</html>
```